Full service residential and commercial painting
Finest quality attention to detail
All workmanship guaranteed
Email :brunomdufay@postvale.fr
Mobile: 0417386250
Industry/Entity Type
Residential
Contact Information for Business Card
Marten Dufay painting & decorating
Requirements
Nice to have
- Am thinking about someone can be painting my name on the card with MD painting with the logos of brush,pot tray and roller sleeves

```html
<!DOCTYPE html>
<html lang="en">
<head>
<meta charset="utf-8">
<title>Marten Dufay painting &amp; decorating – business card</title>
<link rel="stylesheet" href="https://fonts.googleapis.com/css2?family=Cormorant+Garamond:ital,wght@1,500;1,600&display=swap">
<style>
  :root {
    --backdrop: #e9c3ad;
    --card: #fdfcf8;
    --ink: #161616;
    --pink: 221, 143, 198;
    --green: 159, 210, 126;
    --teal: 114, 207, 207;
    --yellow: 246, 224, 79;
    --silhouette: #1b1b1b;
    --roller: #a9d88f;
    --pot: #e7a6d4;
  }
  * { margin: 0; padding: 0; box-sizing: border-box; }
  html, body {
    width: 1200px; height: 1000px; overflow: hidden;
    background: var(--backdrop);
  }
  .business-card {
    position: absolute; left: 150px; top: 240px;
    width: 900px; height: 520px;
    background: var(--card);
    border-radius: 28px;
    box-shadow: 0 10px 30px rgba(80, 40, 20, 0.25);
    overflow: hidden;
    font-family: "Cormorant Garamond", Georgia, serif;
    font-style: italic;
    color: var(--ink);
  }
  .art { position: absolute; }
  .splash-pink {
    left: 40px; top: 0; width: 320px; height: 520px;
    background: radial-gradient(closest-side, rgba(var(--pink), .8) 0%, rgba(var(--pink), .3) 55%, rgba(var(--pink), 0) 100%);
  }
  .splash-green {
    left: 260px; top: 120px; width: 420px; height: 340px;
    background: radial-gradient(closest-side, rgba(var(--green), .85) 0%, rgba(var(--green), .35) 55%, rgba(var(--green), 0) 100%);
  }
  .splash-teal {
    left: 460px; top: 200px; width: 340px; height: 320px;
    background: radial-gradient(closest-side, rgba(var(--teal), .8) 0%, rgba(var(--teal), .3) 55%, rgba(var(--teal), 0) 100%);
  }
  .splash-yellow {
    left: 620px; top: 0; width: 320px; height: 560px;
    background: radial-gradient(closest-side, rgba(var(--yellow), .85) 0%, rgba(var(--yellow), .35) 55%, rgba(var(--yellow), 0) 100%);
  }
  .painter-figure {
    left: 40px; top: 60px; width: 140px; height: 290px;
    border-radius: 40% 40% 20% 20%;
    background: linear-gradient(180deg, #2a2a2a, var(--silhouette));
    opacity: .9;
  }
  .roller-tool {
    left: 740px; top: 150px; width: 80px; height: 240px;
    border-radius: 20px;
    background: linear-gradient(180deg, #3a3a3a 0%, #6a6a6a 55%, var(--roller) 75%, var(--roller) 100%);
    opacity: .85;
  }
  .pot-and-brush {
    left: 620px; top: 370px; width: 180px; height: 130px;
    border-radius: 18px;
    background: linear-gradient(135deg, var(--pot) 0%, #bfe3e3 55%, #e8e8e8 100%);
    opacity: .9;
  }
  .brand-name {
    position: absolute; left: 300px; top: 40px;
    font-size: 64px; font-weight: 600; letter-spacing: 1px; line-height: 1.1;
  }
  .brand-trade {
    position: absolute; left: 440px; top: 125px;
    font-size: 34px; font-weight: 500; line-height: 1.1;
    text-decoration: underline; text-underline-offset: 6px;
  }
  .services {
    position: absolute; left: 200px; top: 205px; width: 520px;
    text-align: center; font-size: 27px; font-weight: 500; line-height: 1.05;
  }
  .contact {
    position: absolute; left: 200px; top: 370px;
    font-size: 30px; font-weight: 500; line-height: 1.15;
  }
</style>
</head>
<body>
  <article class="business-card">
    <div class="art splash-yellow" role="img" aria-label="Yellow watercolour paint splatter"></div>
    <div class="art splash-pink" role="img" aria-label="Pink watercolour paint splash with drips"></div>
    <div class="art splash-green" role="img" aria-label="Green paint splatter"></div>
    <div class="art splash-teal" role="img" aria-label="Turquoise paint splash with drips"></div>
    <div class="art painter-figure" role="img" aria-label="Silhouette of a painter reaching up with a brush"></div>
    <div class="art roller-tool" role="img" aria-label="Paint roller illustration"></div>
    <div class="art pot-and-brush" role="img" aria-label="Paint pot with pink drips and a paintbrush"></div>

    <h1 class="brand-name">Marten Dufay</h1>
    <p class="brand-trade">painting &amp; decorating</p>

    <p class="services">
      Full service residential and commercial painting<br>
      Finest quality attention to detail<br>
      All workmanship guaranteed
    </p>

    <p class="contact">
      Email :brunomdufay@postvale.fr<br>
      Mobile: 0417386250
    </p>
  </article>
</body>
</html>
```